Financial Services Firm - Prospective Partnership Marketing Brochure

What business are we in? Lantern Grove Financial Management (LGM) was founded to provide payroll, bookkeeping, bill paying, debt management, and financial aggregation services for individuals and small businesses seeking relief from the details associated with their financial matters — clerical tasks that our customers either cannot or prefer not to perform. At its core, our service is often referred to as Daily Money Management. As leaders in the Daily Money Management field, we leverage financial controls, technology and concierge-like personal attention in order to maximize the convenience our service provides for our business and individual clients. LGM complements the work of other professionals by completing day-to-day tasks rather than long-term plans. The services meet a continuum of needs, from organizing and keeping track of financial information, book keeping, and investment tracking, to assisting with bill paying and maintaining bank accounts and insurance.
We need a design for a marketing brochure with the following specs:
Four-panel brochure with a double gatefold.
➢ Unfolded: 15 x 9
➢ Finished size: 3 3/4 x 9
Purpose - To convey key information about LGM.
“Look and feel” - Needs to be professional, “corporate” and information showcased must be “top-line”.
Primary Targets - High net-worth individuals, small business owners, on-the-go professionals and individuals
Purpose - To convey key information about LGM to potential business partners.
“Look and feel” - Needs to be professional, “corporate” and information showcased must be “top-line”. These are busy professional people, so less is more.
Primary Targets – Financial Planners
Current company logo, letterhead, business card design, and brochure content details attached for reference.

```html
<!DOCTYPE html>
<html lang="en">
<head>
<meta charset="utf-8">
<title>Lantern Grove Financial Management – Partner Brochure</title>
<link rel="stylesheet" href="https://fonts.googleapis.com/css2?family=Open+Sans:wght@300;400;600;700;800&display=swap">
<style>
  :root{
    --backdrop:#2a2a2a;
    --panel-dark:#3c3c3c;
    --panel-mid:#4a4a4a;
    --panel-grey:#6f6f6f;
    --panel-grey-light:#838383;
    --bar-black:#0d0d0d;
    --accent-blue:#2aa2d8;
    --accent-orange:#e0924a;
    --tagline-tan:#ecc9a0;
    --text-white:#ffffff;
    --text-soft:#dcdcdc;
    --logo-grey:#3a3a3a;
  }
  *{margin:0;padding:0;box-sizing:border-box}
  html,body{width:1200px;height:793px;overflow:hidden}
  body{background:var(--backdrop);font-family:"Open Sans",Arial,sans-serif;color:var(--text-white);position:relative}
  .brochure{position:absolute;left:62px;top:73px;width:1078px;height:647px}
  .panel{position:absolute;top:0;height:647px;overflow:hidden}

  /* Panel 1 – contact & call to action */
  .panel-contact{left:0;width:269px;background:var(--panel-dark)}
  .contact-top{position:absolute;left:0;top:0;width:269px;height:267px;background:var(--panel-mid)}
  .contact-rule{position:absolute;left:0;top:270px;width:269px;height:3px;background:#5c5c5c}
  .brand-small{position:absolute;left:0;top:44px;width:269px;text-align:center}
  .brand-small .mark{display:inline-block;width:14px;height:14px;background:var(--accent-blue);vertical-align:middle;margin-right:6px}
  .brand-small .name{font-size:14px;font-weight:700;color:var(--text-white);letter-spacing:1px;vertical-align:middle}
  .brand-small .sub{display:block;font-size:8px;font-weight:700;color:var(--text-white);margin-top:4px;letter-spacing:.3px}
  .contact-list{position:absolute;left:55px;top:134px;width:170px;text-align:center;font-size:6.5px;line-height:9px;color:var(--text-soft)}
  .contact-list b{color:var(--text-white)}
  .photo-woman{position:absolute;left:0;top:262px;width:190px;height:385px;
    background:
      radial-gradient(ellipse 60% 35% at 30% 20%,rgba(96,70,55,.9) 0%,rgba(96,70,55,0) 100%),
      linear-gradient(180deg,#4b3b31 0%,#6e5a4e 30%,#8a8c95 55%,#9a9ea7 75%,#6f737c 100%)}
  .cta-head{position:absolute;left:98px;top:286px;width:170px;font-weight:300;line-height:1}
  .cta-head .l1{font-size:19px;display:block}
  .cta-head .l2{font-size:24px;display:block;margin-top:3px}
  .cta-head .l3{font-size:36px;display:block;margin-top:1px}
  .cta-body{position:absolute;left:100px;top:390px;width:160px;text-align:center;font-size:10.5px;line-height:14px;color:var(--text-white)}
  .cta-body b{font-weight:700}
  .cta-note{position:absolute;left:112px;top:443px;width:150px;text-align:center;font-size:10.5px;line-height:14px;color:var(--text-soft);font-weight:300}
  .cta-note small{font-size:7px;line-height:8px}
  .office-hours{position:absolute;right:9px;top:588px;text-align:right;font-size:7.5px;line-height:9.5px}
  .office-hours b{font-weight:700}

  /* Panels 2 & 3 – inside spread */
  .photo-spread{position:absolute;left:269px;top:0;width:541px;height:275px;
    background:
      radial-gradient(ellipse 30% 55% at 58% 60%,rgba(240,240,242,.85) 0%,rgba(240,240,242,0) 100%),
      linear-gradient(90deg,rgba(255,255,255,.25) 0%,rgba(255,255,255,0) 40%,rgba(255,255,255,.2) 100%),
      linear-gradient(180deg,#e4e8ea 0%,#c9d1d5 35%,#9fb0b8 65%,#6f8893 100%)}
  .photo-spread-mark{position:absolute;left:752px;top:234px;font-size:8px;font-weight:700;color:var(--text-white);letter-spacing:.3px}
  .panel-service{left:269px;top:275px;width:270px;height:345px;background:var(--panel-mid)}
  .panel-benefits{left:539px;top:275px;width:271px;height:345px;background:linear-gradient(180deg,var(--panel-grey) 0%,var(--panel-grey-light) 100%)}
  .service-kicker{position:absolute;left:19px;top:11px;font-size:9.5px;font-weight:700;color:var(--accent-blue)}
  .service-head{position:absolute;left:19px;top:24px;width:240px;font-size:20px;font-weight:300;line-height:21px}
  .service-intro{position:absolute;left:19px;top:107px;width:225px;font-size:10px;line-height:14px;color:var(--text-soft)}
  .service-lead{position:absolute;left:19px;top:170px;width:230px;font-size:8px;line-height:11px;color:var(--text-soft)}
  .increase-list{position:absolute;left:15px;top:200px;list-style:none;font-size:8px;line-height:12px;color:var(--text-soft)}
  .increase-list li{height:12px}
  .increase-list .tag{display:inline-block;width:57px;height:12px;background:var(--accent-blue);color:var(--text-white);font-weight:700;font-size:10px;line-height:12px;padding-left:3px;margin-right:5px}
  .service-body{position:absolute;left:19px;top:253px;width:232px;font-size:7px;line-height:10px;color:var(--text-soft)}
  .benefits-head{position:absolute;left:22px;top:9px;width:240px;line-height:1}
  .benefits-head .big{display:block;font-size:29px;font-weight:800;letter-spacing:.2px}
  .benefits-head .small{display:block;font-size:19px;font-weight:300;line-height:21px;margin-top:2px}
  .benefit{position:absolute;left:22px;width:232px}
  .benefit h3{font-size:11px;font-weight:700;line-height:14px}
  .benefit p{font-size:7px;font-weight:600;line-height:9px;color:var(--text-soft)}
  .bottom-bar{position:absolute;left:269px;top:620px;width:809px;height:27px;background:var(--bar-black);font-size:8.5px;color:var(--text-white)}
  .bottom-bar span{position:absolute;top:8px}

  /* Panel 4 – cover */
  .panel-cover{left:810px;top:0;width:268px;height:620px;
    background:
      radial-gradient(ellipse 40% 30% at 80% 55%,rgba(30,35,55,.55) 0%,rgba(30,35,55,0) 100%),
      linear-gradient(180deg,#a9a396 0%,#8f897c 22%,#6e685c 40%,#7a6c4f 55%,#6b5c3c 72%,#4f4630 100%)}
  .cover-brand{position:absolute;left:0;top:110px;width:268px;text-align:center}
  .cover-brand .mark{display:inline-block;width:18px;height:18px;background:var(--accent-blue);vertical-align:middle;margin-right:7px}
  .cover-brand .name{font-size:22px;font-weight:700;color:var(--logo-grey);letter-spacing:1px;vertical-align:middle}
  .cover-brand .sub{display:block;font-size:13px;font-weight:700;color:var(--logo-grey);margin-top:8px}
  .cover-tagline{position:absolute;left:26px;top:213px;width:170px;font-size:10.5px;line-height:14px;color:var(--tagline-tan)}
  .cover-tagline b{color:var(--accent-orange);font-weight:700}
</style>
</head>
<body>
<main class="brochure">

  <section class="panel panel-contact">
    <div class="contact-top"></div>
    <div class="brand-small"><span class="mark"></span><span class="name">LANTERN GROVE</span><span class="sub">Financial Management</span></div>
    <p class="contact-list">
      <b>P:</b> (555) 014-2290<br>
      <b>M:</b> info@lanterngrovefm.com<br>
      <b>A:</b> Lantern Grove Financial Management, 2100 N.<br>Orchard Lane, Fairview, AZ 85000
    </p>
    <div class="contact-rule"></div>
    <div class="photo-woman" role="img" aria-label="Photo of a smiling businesswoman in a grey suit with arms crossed"></div>
    <h2 class="cta-head"><span class="l1">BECOME AN</span><span class="l2">LGM PARTNER</span><span class="l3">TODAY!</span></h2>
    <p class="cta-body"><b>For a free consultation</b> on becoming an LGM Partner, contact us today.</p>
    <p class="cta-note">An LGM representative will normally respond to all inquiries within 2 to 24 hours <small>(excluding weekends and holidays).</small></p>
    <p class="office-hours"><b>LGM office hours:</b><br>Monday - Friday<br>from 9:00 AM to 5:00 PM MST.</p>
  </section>

  <div class="photo-spread" role="img" aria-label="Photo of a relaxed, smiling businessman with hands behind his head in a bright office"></div>
  <span class="photo-spread-mark">LGM</span>

  <section class="panel panel-service">
    <p class="service-kicker">Daily Money Management:</p>
    <h2 class="service-head">THE MOST IMPORTANT SERVICE YOU NEVER KNEW ABOUT.</h2>
    <p class="service-intro">Have you ever sat at your desk flipping through the chaos of papers your clients or prospects hand you, trying to find the necessary information you need for financial planning?</p>
    <p class="service-lead">Lantern Grove Financial Management (LGM), a Daily Money Management service, can discuss how you can:</p>
    <ul class="increase-list">
      <li><span class="tag">Increase</span>your firm's efficiencies.</li>
      <li><span class="tag">Increase</span>your client base.</li>
      <li><span class="tag">Increase</span>your value proposition to your clients.</li>
    </ul>
    <p class="service-body">LGM is your extra right hand while providing your clients with greater independence and accuracy in managing their finances. We help your clients beyond the typical organization of financial records by filing insurance and medical claims, or giving personalized attention around instituting a spending plan.</p>
  </section>

  <section class="panel panel-benefits">
    <h2 class="benefits-head"><span class="big">THE BENEFITS</span><span class="small">OF PARTNERING WITH LGM:</span></h2>
    <div class="benefit" style="top:105px"><h3>- LGM performs daily money management and data aggregation services for your clients.</h3><p>- We complement your work and leave you free to focus on your core business.</p></div>
    <div class="benefit" style="top:196px"><h3>- LGM brings you clients.</h3><p>– By working with an array of professional partners we expand each other's client pools.</p></div>
    <div class="benefit" style="top:255px"><h3>- LGM adds value to your firm.</h3><p>- We provide the added services your clients' want; keeping them organized &amp; feeling in control.</p></div>
  </section>

  <section class="panel panel-cover" role="img" aria-label="Photo of a businessman in a suit shading his eyes, standing on a grassy hill under a hazy sky">
    <div class="cover-brand"><span class="mark"></span><span class="name">LANTERN GROVE</span><span class="sub">Financial Management</span></div>
    <p class="cover-tagline"><b>Expanding your Financial</b><br>Planning business<br>begins with a<br>…Lantern Grove.</p>
  </section>

  <footer class="bottom-bar">
    <span style="left:29px">Become an LGM partner by calling (555) 014-2290</span>
    <span style="left:345px">www.lanterngrovefm.com</span>
    <span style="left:624px">www.lanterngrovefm.com</span>
  </footer>

</main>
</body>
</html>
```